Unique Business Card Design

Unique Business Card design for our orthotic and prosthetic company. Our logo is on our website, color is light blue. Unique shape (artificial leg shaped, vertical, etc..) preferred. Logo, business name, individual name and basic demographics needed.

Industry/Entity Type

Business

Contact Information for Business Card

Logo, Industry, Phone # Logo, "Prosthetic & Orthotic Services" Place to add individual name and contact info

Colors
cee9f5

Requirements
Must have
• The icon must be there, placement of "Prosthetic & Orthotic Services" can be moved
Nice to have
• Like the mix of light blue, and a little darker blue. One design included the icons from my website which was a nice touch

```html
<!DOCTYPE html>
<html lang="en">
<head>
<meta charset="utf-8">
<title>LimbWorks Inc. — Business Card</title>
<link rel="stylesheet" href="https://fonts.googleapis.com/css2?family=Open+Sans:wght@400;600&family=Roboto:wght@400;500&family=Crimson+Text:ital@1&display=swap">
<style>
  :root {
    --page-bg: #e4e4e4;
    --card-dark-1: #3a3a3a;
    --card-dark-2: #222222;
    --ice-blue: #cee9f5;
    --ice-blue-text: #d6ecf6;
    --brand-blue: #0b5ca9;
    --name-blue: #1a55a0;
    --ink: #2b2b2b;
    --rule: #d4d4d4;
    --white: #ffffff;
  }
  * { margin: 0; padding: 0; box-sizing: border-box; }
  html, body { width: 1200px; height: 1000px; overflow: hidden; }
  body { background: var(--page-bg); position: relative; font-family: "Roboto", Arial, sans-serif; }

  .card {
    position: absolute; left: 220px; width: 760px; height: 435px;
    border-radius: 28px; overflow: hidden;
    box-shadow: 0 6px 18px rgba(0,0,0,.25);
  }
  .card-back { top: 50px; background: linear-gradient(135deg, var(--card-dark-1), var(--card-dark-2)); }
  .card-front { top: 523px; background: var(--white); }

  .abs { position: absolute; }

  /* back */
  .back-badge { left: 138px; top: 111px; width: 130px; height: 130px; border-radius: 50%; background: var(--ice-blue); }
  .back-name { left: 285px; top: 126px; font-family: "Open Sans", Arial, sans-serif; font-weight: 600; font-size: 38px; color: var(--ice-blue-text); letter-spacing: .5px; white-space: nowrap; }
  .back-rule { left: 285px; top: 177px; width: 334px; height: 3px; background: var(--ice-blue-text); }
  .back-tagline { left: 307px; top: 183px; font-family: "Crimson Text", Georgia, serif; font-style: italic; font-size: 23px; color: var(--ice-blue-text); white-space: nowrap; }

  .service { top: 309px; width: 130px; text-align: center; }
  .service-orb { width: 58px; height: 58px; margin: 0 auto; border-radius: 50%;
    background: radial-gradient(circle at 35% 30%, #f4fbfe, var(--ice-blue) 60%, #9fc6d8); }
  .service-label { margin-top: 9px; font-size: 15.5px; color: var(--ice-blue-text); letter-spacing: .3px; }
  .service-1 { left: 188px; } .service-2 { left: 320px; } .service-3 { left: 444px; }

  /* front */
  .front-badge { left: 43px; top: 43px; width: 84px; height: 84px; border-radius: 50%; background: var(--brand-blue); }
  .front-name { left: 137px; top: 55px; font-family: "Open Sans", Arial, sans-serif; font-weight: 600; font-size: 24px; color: var(--brand-blue); white-space: nowrap; }
  .front-rule { left: 137px; top: 86px; width: 214px; height: 2px; background: var(--brand-blue); }
  .front-tagline { left: 152px; top: 90px; font-family: "Crimson Text", Georgia, serif; font-style: italic; font-size: 15px; color: var(--brand-blue); white-space: nowrap; }

  .person { left: 137px; top: 146px; }
  .person-name { font-weight: 500; font-size: 22px; color: var(--name-blue); }
  .person-title { font-size: 16.5px; color: var(--ink); margin-top: 2px; }
  .person-rule { left: 137px; top: 203px; width: 188px; height: 1px; background: var(--rule); }

  .address { left: 137px; top: 218px; font-size: 17px; line-height: 22px; color: var(--ink); }

  .contacts { left: 137px; top: 276px; list-style: none; font-size: 17px; color: var(--ink); }
  .contacts li { display: flex; align-items: center; height: 24.4px; }
  .contacts svg { width: 13px; height: 13px; margin-right: 7px; fill: var(--name-blue); flex: none; }
  .contacts .web-domain { color: var(--brand-blue); }

  .front-arc { left: 416px; top: -28px; width: 490px; height: 490px; border-radius: 50%; background: var(--brand-blue); }
</style>
</head>
<body>

<section class="card card-back" aria-label="Card back">
  <div class="abs back-badge"></div>
  <div class="abs back-name">LIMBWORKS INC.</div>
  <div class="abs back-rule"></div>
  <div class="abs back-tagline">Prosthetic &amp; Orthotic Services</div>

  <div class="abs service service-1">
    <div class="service-orb" role="img" aria-label="Orthotics icon of a knee joint"></div>
    <div class="service-label">Orthotics</div>
  </div>
  <div class="abs service service-2">
    <div class="service-orb" role="img" aria-label="Prosthetics icon of a standing figure"></div>
    <div class="service-label">Prosthetics</div>
  </div>
  <div class="abs service service-3">
    <div class="service-orb" role="img" aria-label="Vascular icon of a wheelchair"></div>
    <div class="service-label">Vascular</div>
  </div>
</section>

<section class="card card-front" aria-label="Card front">
  <div class="abs front-arc" role="img" aria-label="Large blue brand circle decoration"></div>

  <div class="abs front-badge"></div>
  <div class="abs front-name">LIMBWORKS INC.</div>
  <div class="abs front-rule"></div>
  <div class="abs front-tagline">Prosthetic &amp; Orthotic Services</div>

  <div class="abs person">
    <div class="person-name">Miriam Castell</div>
    <div class="person-title">CO LPO</div>
  </div>
  <div class="abs person-rule"></div>

  <div class="abs address">2260 Linden Avenue<br>Brookvale, NY 11230</div>

  <ul class="abs contacts">
    <li><svg viewBox="0 0 16 16"><path d="M4 0h8a1.5 1.5 0 0 1 1.5 1.5v13A1.5 1.5 0 0 1 12 16H4a1.5 1.5 0 0 1-1.5-1.5v-13A1.5 1.5 0 0 1 4 0zm0 2v11h8V2zm4 11.6a.9.9 0 1 0 0 1.8.9.9 0 0 0 0-1.8z"/></svg>555-0142188</li>
    <li><svg viewBox="0 0 16 16"><path d="M3.5 1l2.6 3.2-1.5 1.7a9 9 0 0 0 5.5 5.5l1.7-1.5L15 12.5 13 15C6.5 14.5 1.5 9.5 1 3z"/></svg>(555) 014-2200</li>
    <li><svg viewBox="0 0 16 16"><path d="M4 0h8v4H4zM1 5h14v7h-3v4H4v-4H1zm5 6v3h4v-3z"/></svg>(555) 014-2201</li>
    <li><svg viewBox="0 0 16 16"><path d="M0 3h16v1.5L8 9 0 4.5zm0 3.3l8 4.4 8-4.4V13H0z"/></svg>Mcastell@limbworksinc.com</li>
    <li><svg viewBox="0 0 16 16"><path d="M8 0a8 8 0 1 0 0 16A8 8 0 0 0 8 0zm0 1.5c.9 0 1.9 1.9 2.2 5H5.8C6.1 3.4 7.1 1.5 8 1.5zM1.6 7.2h2.7c0-1.8.3-3.4.9-4.6A6.5 6.5 0 0 0 1.6 7.2zm0 1.6a6.5 6.5 0 0 0 3.6 4.6c-.6-1.2-.9-2.8-.9-4.6zm4.2 0c.3 3.1 1.3 5.7 2.2 5.7s1.9-2.6 2.2-5.7zm5.9 0c0 1.8-.3 3.4-.9 4.6a6.5 6.5 0 0 0 3.6-4.6zm2.7-1.6a6.5 6.5 0 0 0-3.6-4.6c.6 1.2.9 2.8.9 4.6z"/></svg>www.<span class="web-domain">limbworksinc</span>.net</li>
  </ul>
</section>

</body>
</html>
```